WordPress Website for Accounting Firm

I have attached an excel sheet showing what i need done for my accounting website. Currently i have a WP website but its not live and do not like it. I can give a link if that will help. Total pages is around 12. I can buy and supply the images but have provided indication of what i want in the excel. I will need the designer to do the coding to make the website fully functional. I want a clean look and attractive. Don't want too dark colors. Once i like the landing page, i will need the designer to code code the website. Just want to look first. I will provide the logo file and put the contents myself. Just put dummy contents for now to show how it will look.
Can you please use the attached images so i can see how nit will look on the coverage as an option. These are from pixelharbor
903516284
475120968
2067391145
1830647729
Currently there are only 2 provided by myself as Photo 1 and Photo 2
Many Thanks!
Accounting and Finance
5+ page

```html
<!DOCTYPE html>
<html lang="en">
<head>
<meta charset="utf-8">
<title>Ledgerwell — Tax &amp; Accounting</title>
<link href="https://fonts.googleapis.com/css2?family=Outfit:wght@300;400;500;600;700;800&display=swap" rel="stylesheet">
<style>
:root{
  --green:#4e9a43;
  --green-pale:#e9f2e8;
  --green-soft:#cfe4cc;
  --paper:#f6f8f5;
  --nav:#f5f5f3;
  --ink:#151515;
  --text:#3a3a3a;
  --white:#ffffff;
  --divider:#cfcfcf;
}
*{box-sizing:border-box;margin:0;padding:0}
html,body{width:1200px;height:3071px;overflow:hidden}
body{font-family:"Outfit",sans-serif;color:var(--text);background:var(--white);position:relative}
.btn{position:absolute;display:flex;align-items:center;justify-content:center;background:var(--green);color:var(--white);border-radius:20px;font-size:16px;font-weight:400}
.brand{position:absolute;display:flex;align-items:center;gap:8px;font-weight:500;letter-spacing:.5px}
.brand .mark{width:34px;height:34px;border-radius:50%;background:var(--green)}

/* nav */
.site-nav{position:absolute;left:0;top:0;width:1200px;height:67px;background:var(--nav)}
.site-nav .brand{left:116px;top:17px;color:#555;font-size:18px}
.nav-link{position:absolute;top:26px;font-size:13px;font-weight:500;color:var(--ink);letter-spacing:.2px}
.nav-link.active{border-bottom:2px solid var(--green);padding-bottom:3px}
.nav-cta{left:960px;top:17px;width:124px;height:33px;font-size:13px;font-weight:500}

/* hero */
.hero-photo{position:absolute;left:0;top:67px;width:1200px;height:660px;
  background:radial-gradient(circle at 1000px 260px,#f39a2c 0,#d2562a 18%,transparent 40%),
  radial-gradient(circle at 720px 300px,#b98a77 0,#6e3a3c 25%,transparent 45%),
  linear-gradient(100deg,#2a1a22 0%,#5a1f2a 35%,#4a2c3c 60%,#7a3a2a 100%)}
.hero-curve{position:absolute;left:0;top:600px}
.hero-title{position:absolute;left:161px;top:222px;color:var(--white);font-weight:800;font-size:80px;line-height:78px;letter-spacing:-.5px}
.hero-sub{position:absolute;left:161px;top:402px;color:var(--white);font-size:27px;font-weight:300}
.hero-btn{left:160px;top:467px;width:136px;height:37px}
.hero-next{position:absolute;left:1047px;top:326px;width:48px;height:48px;border-radius:50%;background:rgba(78,154,67,.85)}
.scroll-cue{position:absolute;left:561px;top:673px;width:76px;height:76px;border-radius:50%;background:var(--white);border:2px solid var(--green);box-shadow:0 3px 10px rgba(0,0,0,.12)}

/* shared titles */
.section-title{font-weight:800;font-size:43px;color:var(--ink);letter-spacing:-.5px}
.section-title .light{font-weight:400}
.rule{position:absolute;height:3px;background:var(--green)}

/* about */
.about{position:absolute;left:0;top:727px;width:1200px;height:501px;background:var(--paper)}
.about-photo{position:absolute;left:158px;top:780px;width:337px;height:376px;border-radius:50%;
  background:linear-gradient(160deg,#8cb6d8 0%,#c9a37c 30%,#6f8a4a 55%,#8a6a4f 80%,#7a746a 100%)}
.about-title{position:absolute;left:597px;top:826px}
.about-lead{position:absolute;left:597px;top:884px;font-size:16px;color:var(--ink)}
.about-copy{position:absolute;left:597px;width:450px;font-size:13px;line-height:24.5px;color:#4a4a4a}
.about-copy.dark{color:var(--ink)}

/* why */
.why{position:absolute;left:0;top:1228px;width:1200px;height:589px;background:var(--green-pale)}
.why-title{position:absolute;left:122px;top:1358px;font-weight:700}
.why-list{position:absolute;left:116px;top:1456px;width:500px;list-style:none;font-size:15px;line-height:23px;color:#333}
.why-list li{position:relative;padding-left:25px;margin-bottom:14px}
.why-list li:first-child,.why-list li:nth-child(2){padding-right:80px}
.why-list svg{position:absolute;left:0;top:4px}
.why-btn{left:116px;top:1666px;width:135px;height:37px}
.blob-light{position:absolute;left:704px;top:1343px;width:390px;height:390px;border-radius:50%;background:var(--green-soft)}
.blob-dark{position:absolute;left:836px;top:1291px;width:200px;height:170px;border-radius:50%;background:var(--green)}
.why-photo{position:absolute;left:715px;top:1326px;width:368px;height:369px;border-radius:30px;
  background:radial-gradient(circle at 330px 150px,#f39a2c 0,#d2562a 25%,transparent 50%),
  linear-gradient(110deg,#2a2a3a 0%,#6a3a3a 45%,#9a6a5a 70%,#c8602a 100%)}

/* testimonial */
.hand{position:absolute;border-radius:40px;background:linear-gradient(160deg,#f1cdb3,#d9a383)}
.proof-title{position:absolute;left:200px;top:2002px;width:240px;text-align:center;font-weight:700;font-size:35px;line-height:36px;color:#2a2a2a;letter-spacing:-.5px}
.proof-title .accent{color:var(--green)}
.proof-divider{position:absolute;left:579px;top:1903px;width:1px;height:317px;background:var(--divider)}
.avatar{position:absolute;left:812px;top:1911px;width:96px;height:96px;border-radius:50%;border:3px solid var(--green);background:linear-gradient(160deg,#e39a5a,#7a4a3a)}
.quote-mark{position:absolute;font-size:40px;font-weight:800;color:#2a2a2a;line-height:1}
.quote-text{position:absolute;left:658px;top:2025px;width:412px;text-align:center;font-size:11.5px;line-height:21px;color:#444}
.quote-name{position:absolute;left:658px;top:2145px;width:412px;text-align:center;font-size:14px;color:var(--ink)}
.dot-nav{position:absolute;top:2196px;width:10px;height:10px;border-radius:50%;background:var(--green)}
.dot-nav.off{background:var(--white);border:1.5px solid var(--green)}

/* industries */
.industries{position:absolute;left:0;top:2306px;width:1200px;height:492px;background:var(--paper)}
.ind-title{position:absolute;left:0;top:2383px;width:1200px;text-align:center}
.ind-sub{position:absolute;left:0;top:2441px;width:1200px;text-align:center;font-size:16px;font-weight:400;color:var(--ink)}
.ind-card{position:absolute;top:2516px;width:203px;height:169px;background:var(--white);border-radius:6px;box-shadow:0 4px 14px rgba(0,0,0,.05);list-style:none;padding:34px 0 0 27px;font-size:12.5px;color:#333}
.ind-card.tinted{background:var(--green-pale)}
.ind-card li{display:flex;align-items:center;gap:10px;height:37px}

/* footer */
.site-footer{position:absolute;left:0;top:2798px;width:1200px;height:273px;background:var(--green);color:var(--white)}
.site-footer .brand{left:158px;top:54px;color:var(--white);font-size:19px}
.site-footer .brand .mark{background:var(--white)}
.social{position:absolute;top:133px;width:18px;height:18px;border-radius:50%;background:var(--white)}
.foot-col{position:absolute;top:48px}
.foot-col h4{font-size:15px;font-weight:600;margin-bottom:14px}
.foot-col ul{list-style:none}
.foot-col li{font-size:10.5px;line-height:19.5px;letter-spacing:.3px}
.foot-bottom{position:absolute;top:228px;font-size:11.5px}
</style>
</head>
<body>

<header class="site-nav">
  <div class="brand"><span class="mark"></span>LEDGERWELL</div>
  <span class="nav-link active" style="left:546px">HOME</span>
  <span class="nav-link" style="left:615px">SOLUTIONS</span>
  <span class="nav-link" style="left:720px">CLIENTS</span>
  <span class="nav-link" style="left:804px">CLIENT RESOURSES</span>
  <span class="btn nav-cta">CONTACT US</span>
</header>

<section>
  <div class="hero-photo" role="img" aria-label="Woman smiling at her phone with glowing data overlays"></div>
  <svg class="hero-curve" width="1200" height="130" viewBox="0 600 1200 130">
    <path d="M0,655 Q600,770 1200,655 L1200,730 L0,730 Z" fill="#f6f8f5"/>
    <path d="M0,658 Q600,780 1200,660" fill="none" stroke="#4e9a43" stroke-width="6"/>
  </svg>
  <h1 class="hero-title">Tax &amp;<br>Accounting</h1>
  <p class="hero-sub">Services for a Variety of Industries.</p>
  <span class="btn hero-btn">Learn More</span>
  <div class="hero-next">
    <svg width="48" height="48"><path d="M21 15 L30 24 L21 33" fill="none" stroke="#e8f3e6" stroke-width="3"/></svg>
  </div>
</section>

<div class="about"></div>
<div class="scroll-cue">
  <svg width="72" height="72"><rect x="30" y="18" width="12" height="22" rx="6" fill="none" stroke="#222" stroke-width="1.8"/><line x1="36" y1="23" x2="36" y2="28" stroke="#222" stroke-width="1.8"/><path d="M32 43 L36 47 L40 43 M32 48 L36 52 L40 48" fill="none" stroke="#222" stroke-width="1.5"/></svg>
</div>
<section>
  <div class="about-photo" role="img" aria-label="Mountain landscape photograph"></div>
  <h2 class="section-title about-title">About <span class="light">Us</span></h2>
  <p class="about-lead">Lorem Ipsum is simply dummy text of the printing.</p>
  <div class="rule" style="left:597px;top:914px;width:54px"></div>
  <p class="about-copy" style="top:938px">Lorem Ipsum is simply dummy text of the printing and typesetting industry. Lorem Ipsum has been the industry's standard dummy text ever since the 1500s, when an unknown printer took a galley of type and scrambled it to make a type specimen book. It has survived not only five centuries,</p>
  <p class="about-copy dark" style="top:1051px">Lorem Ipsum is simply dummy text of the printing and typesetting industry. Lorem Ipsum has been the industry's standard dummy text</p>
</section>

<section class="why"></section>
<h2 class="section-title why-title">WHY <span class="light">CHOOSE Us</span></h2>
<div class="rule" style="left:122px;top:1420px;width:54px"></div>
<ul class="why-list">
  <li><svg width="14" height="14"><circle cx="7" cy="7" r="7" fill="#4e9a43"/><path d="M4 7 L6 9 L10 5" fill="none" stroke="#fff" stroke-width="1.6"/></svg>We specialise in accounting and tax solutions for all business structures and industries</li>
  <li><svg width="14" height="14"><circle cx="7" cy="7" r="7" fill="#4e9a43"/><path d="M4 7 L6 9 L10 5" fill="none" stroke="#fff" stroke-width="1.6"/></svg>Our team are qualified professionals with 50+ years of combined experience in CA industry</li>
  <li><svg width="14" height="14"><circle cx="7" cy="7" r="7" fill="#4e9a43"/><path d="M4 7 L6 9 L10 5" fill="none" stroke="#fff" stroke-width="1.6"/></svg>We are Accessable 7 days a week</li>
  <li><svg width="14" height="14"><circle cx="7" cy="7" r="7" fill="#4e9a43"/><path d="M4 7 L6 9 L10 5" fill="none" stroke="#fff" stroke-width="1.6"/></svg>We constantly upskill to keep up with changes to tax laws and legislation</li>
</ul>
<span class="btn why-btn">Learn More</span>
<div class="blob-light"></div>
<div class="blob-dark"></div>
<div class="why-photo" role="img" aria-label="Woman looking at her phone with digital light overlays"></div>

<section>
  <div class="hand" style="left:101px;top:1948px;width:120px;height:159px" role="img" aria-label="Hand making an OK gesture"></div>
  <div class="hand" style="left:412px;top:1978px;width:120px;height:173px" role="img" aria-label="Hand making an OK gesture"></div>
  <h2 class="proof-title">Don’t take<br><span class="accent">our word</span><br>for it</h2>
  <div class="proof-divider"></div>
  <div class="avatar" role="img" aria-label="Client portrait"></div>
  <span class="quote-mark" style="left:643px;top:2003px">“</span>
  <p class="quote-text">Lorem Ipsum is simply dummy text of the printing and typesetting industry. Lorem Ipsum has been the industry's standard dummy text ever since the 1500s, when an unknown printer took a galley of type and scrambled it to make a type specimen book. It has survived not only five centuries, but also the leap into electronic typesetting, remaining essentially unchanged.</p>
  <span class="quote-mark" style="left:1026px;top:2118px">”</span>
  <p class="quote-name">Jon Doe</p>
  <span class="dot-nav" style="left:842px"></span>
  <span class="dot-nav off" style="left:855px"></span>
  <span class="dot-nav" style="left:868px"></span>
</section>

<section class="industries"></section>
<h2 class="section-title ind-title">Industries We <span class="light">Represent</span></h2>
<p class="ind-sub">Lorem Ipsum is simply dummy text of the printing.</p>
<div class="rule" style="left:573px;top:2476px;width:54px"></div>
<ul class="ind-card" style="left:148px">
  <li><svg width="13" height="13"><circle cx="6.5" cy="6.5" r="6.5" fill="#4e9a43"/><path d="M3.6 6.6 L5.6 8.6 L9.4 4.6" fill="none" stroke="#fff" stroke-width="1.5"/></svg>Healthcare Specialists</li>
  <li><svg width="13" height="13"><circle cx="6.5" cy="6.5" r="6.5" fill="#4e9a43"/><path d="M3.6 6.6 L5.6 8.6 L9.4 4.6" fill="none" stroke="#fff" stroke-width="1.5"/></svg>Contractors</li>
  <li><svg width="13" height="13"><circle cx="6.5" cy="6.5" r="6.5" fill="#4e9a43"/><path d="M3.6 6.6 L5.6 8.6 L9.4 4.6" fill="none" stroke="#fff" stroke-width="1.5"/></svg>Manufacturing</li>
</ul>
<ul class="ind-card tinted" style="left:381px">
  <li><svg width="13" height="13"><circle cx="6.5" cy="6.5" r="6.5" fill="#4e9a43"/><path d="M3.6 6.6 L5.6 8.6 L9.4 4.6" fill="none" stroke="#fff" stroke-width="1.5"/></svg>Healthcare Specialists</li>
  <li><svg width="13" height="13"><circle cx="6.5" cy="6.5" r="6.5" fill="#4e9a43"/><path d="M3.6 6.6 L5.6 8.6 L9.4 4.6" fill="none" stroke="#fff" stroke-width="1.5"/></svg>Contractors</li>
  <li><svg width="13" height="13"><circle cx="6.5" cy="6.5" r="6.5" fill="#4e9a43"/><path d="M3.6 6.6 L5.6 8.6 L9.4 4.6" fill="none" stroke="#fff" stroke-width="1.5"/></svg>Manufacturing</li>
</ul>
<ul class="ind-card" style="left:615px">
  <li><svg width="13" height="13"><circle cx="6.5" cy="6.5" r="6.5" fill="#4e9a43"/><path d="M3.6 6.6 L5.6 8.6 L9.4 4.6" fill="none" stroke="#fff" stroke-width="1.5"/></svg>Healthcare Specialists</li>
  <li><svg width="13" height="13"><circle cx="6.5" cy="6.5" r="6.5" fill="#4e9a43"/><path d="M3.6 6.6 L5.6 8.6 L9.4 4.6" fill="none" stroke="#fff" stroke-width="1.5"/></svg>Contractors</li>
  <li><svg width="13" height="13"><circle cx="6.5" cy="6.5" r="6.5" fill="#4e9a43"/><path d="M3.6 6.6 L5.6 8.6 L9.4 4.6" fill="none" stroke="#fff" stroke-width="1.5"/></svg>Manufacturing</li>
</ul>
<ul class="ind-card" style="left:848px">
  <li><svg width="13" height="13"><circle cx="6.5" cy="6.5" r="6.5" fill="#4e9a43"/><path d="M3.6 6.6 L5.6 8.6 L9.4 4.6" fill="none" stroke="#fff" stroke-width="1.5"/></svg>Healthcare Specialists</li>
  <li><svg width="13" height="13"><circle cx="6.5" cy="6.5" r="6.5" fill="#4e9a43"/><path d="M3.6 6.6 L5.6 8.6 L9.4 4.6" fill="none" stroke="#fff" stroke-width="1.5"/></svg>Contractors</li>
  <li><svg width="13" height="13"><circle cx="6.5" cy="6.5" r="6.5" fill="#4e9a43"/><path d="M3.6 6.6 L5.6 8.6 L9.4 4.6" fill="none" stroke="#fff" stroke-width="1.5"/></svg>Manufacturing</li>
</ul>

<footer class="site-footer">
  <div class="brand"><span class="mark"></span>LEDGERWELL</div>
  <span class="social" style="left:163px" aria-label="Social link"></span>
  <span class="social" style="left:192px" aria-label="Social link"></span>
  <span class="social" style="left:232px" aria-label="Social link"></span>
  <span class="social" style="left:272px" aria-label="Social link"></span>
  <div class="foot-col" style="left:440px"><h4>Solutions</h4><ul><li>TAX AND ACCOUNTING</li><li>CLOUD ACCOUNTING</li><li>SPECIALIST</li></ul></div>
  <div class="foot-col" style="left:665px"><h4>Clients</h4><ul><li>WHAT CLIENTS SAY</li><li>CLIENT REWARD SCHEME</li><li>INDUSTRIES WE REPRESENT</li></ul></div>
  <div class="foot-col" style="left:909px"><h4>Clients</h4><ul><li>NEWSLETTERS</li><li>WEB LINKS</li><li>COMPLIANCE DOCUMENTS</li></ul></div>
  <p class="foot-bottom" style="left:163px">Copyright @ Ledgerwell &nbsp;|&nbsp; All Rights Reserved.</p>
  <p class="foot-bottom" style="left:919px">Home &nbsp;&nbsp;|&nbsp;&nbsp; Contact Us</p>
</footer>

</body>
</html>
```